Corporate Design für Abwicklung von Lohn- und Gehaltsabrechnungen
Super flexible Zusammenarbeit, alle Änderungen wurden zeitnah zur Ansicht geliefert. Sehr kreatives und einheitliches Ergebnis für das neue CI. Immer wieder gerne!!!
Zielgruppe
Wir wickeln die Lohn- und Gehaltsabrechnung für kleine bis mittlere Unternehmen ab.
Aufgabenstellung
Das bereits bestehende Logo kann gerne noch einmal, aber ähnlich von den Abmessungen und Farben her, geändert werden.
Insgesamt modernes und junges Auftreten.
Wichtig ist das Grün #3dae62
RGB 61 174 98
Wir wünschen uns ein einheitliches Corporate Design bestehend aus Briefpapier, Visitenkarten, Briefumschlägen und Schreibblöcken, angelehnt an das bereits vorhandene Logo.
Briefpapier, gerne 2-seitig mit grüner Rückseite
Endformat 210x297mm hoch
Visitenkarten 2-seitig, 85x55mm quer oder hoch (lassen uns gerne überraschen)
Die beigefügte Visitenkarte ist leider mit alten Daten, hat uns vom Prinzip her aber gut gefallen. Die neue sollte sich aber im Corporate Design Wiederspiegeln mit folgenden Daten:
Briefumschläge C4 (229 x 324mm Endformat) Hoch
Schreibblöcke A5 148x210 Endformat hoch
Schriftart Poppins

```html
<!DOCTYPE html>
<html lang="de">
<head>
<meta charset="utf-8">
<title>Nordwert – Geschäftsausstattung</title>
<link href="https://fonts.googleapis.com/css2?family=Poppins:wght@300;400;500;600&display=swap" rel="stylesheet">
<style>
:root{
  --green:#3dae62;
  --charcoal:#4a4a4a;
  --paper:#f4f4f4;
  --ink:#5a5a5a;
  --stage:#e0e0e0;
  --window:#e6e6e6;
}
*{margin:0;padding:0;box-sizing:border-box}
html,body{width:1200px;height:751px;overflow:hidden}
body{background:var(--stage);font-family:'Poppins',sans-serif;position:relative;color:var(--ink)}
.piece{position:absolute;background:var(--paper);box-shadow:0 3px 8px rgba(0,0,0,.14);overflow:hidden}
.brand-name{font-family:'Poppins',sans-serif;font-weight:500;color:var(--green);line-height:1;position:absolute;white-space:nowrap}
.band{position:absolute;left:0;right:0;bottom:0;height:12px}
.band .g{position:absolute;left:0;bottom:0;height:100%;background:var(--green);border-top-right-radius:8px}
.band .d{position:absolute;right:0;bottom:0;height:70%;background:var(--charcoal)}
.contact{position:absolute;list-style:none}
.contact li{display:flex;align-items:center;white-space:nowrap}
.contact svg{fill:none;stroke:var(--green);stroke-width:1.6;flex:none}

/* business card front */
.card-front{left:158px;top:88px;width:157px;height:88px;background:var(--green)}
.card-front .brand-name{color:#fff;font-size:18px;left:0;right:0;text-align:center;top:34px}
.card-front .url{position:absolute;bottom:7px;left:0;right:0;text-align:center;font-size:4.6px;color:#fff}

/* business card back */
.card-back{left:158px;top:192px;width:158px;height:89px}
.card-back .brand-name{font-size:13px;left:15px;top:11px}
.card-back .name{position:absolute;left:15px;top:41px;font-size:6.4px;font-weight:600;color:var(--green)}
.card-back .role{position:absolute;left:15px;top:49px;font-size:4.8px}
.card-back .address{position:absolute;left:15px;top:62px;font-size:4.2px;line-height:1.35}
.card-back .contact{left:89px;top:42px;font-size:4.2px}
.card-back .contact li{height:8px;gap:4px}
.card-back .band{height:7px}
.card-back .band .g{width:118px;border-top-right-radius:5px}
.card-back .band .d{left:120px}

/* notebook */
.notebook{left:52px;top:319px;width:253px;height:366px;border-radius:3px 14px 10px 3px;background:#f6f6f6}
.notebook .elastic{position:absolute;top:0;bottom:0;left:199px;width:5px;background:#fbfbfb;border-left:1px solid #e2e2e2;border-right:1px solid #e2e2e2}
.notebook .brand-name{font-size:31px;left:32px;top:276px}
.notebook .label{position:absolute;right:80px;top:311px;font-size:14px;line-height:1;font-weight:300;color:var(--charcoal)}
.notebook .band{height:8px}
.notebook .band .g{width:176px;border-top-right-radius:6px}
.notebook .band .d{left:179px;height:80%}
.ribbon{position:absolute;left:68px;top:685px;width:8px;height:64px;background:#f3f3f3;box-shadow:0 1px 3px rgba(0,0,0,.1)}

/* letterhead */
.letterhead{left:368px;top:194px;width:367px;height:519px}
.letterhead .brand-name{font-size:19px;right:24px;top:28px}
.letterhead .address{position:absolute;left:280px;top:71px;font-size:5px;line-height:1.3}
.letterhead .contact{left:280px;top:90px;font-size:5px}
.letterhead .contact li{height:7.6px;gap:4px}
.letterhead .rule{position:absolute;left:22px;top:455px;width:142px;border-top:1px solid #d6d6d6}
.letterhead .legal{position:absolute;top:468px;font-size:3.8px;line-height:1.4;color:#8a8a8a}
.letterhead .legal.tax{left:25px}
.letterhead .legal.bank{left:96px}
.letterhead .band{height:13px}
.letterhead .band .g{width:258px}
.letterhead .band .d{left:261px}

/* envelope */
.envelope{left:782px;top:178px;width:376px;height:533px}
.envelope .brand-name{font-size:21px;left:37px;top:63px}
.envelope .window{position:absolute;left:29px;top:95px;width:153px;height:92px;background:var(--window);border:1px solid #dadada;border-radius:4px}
.envelope .band{height:12px}
.envelope .band .g{width:263px}
.envelope .band .d{left:266px}
</style>
</head>
<body>

<section class="piece card-front" aria-label="Visitenkarte Vorderseite">
  <span class="brand-name">Nordwert</span>
  <span class="url">www.nordwert.eu</span>
</section>

<section class="piece card-back" aria-label="Visitenkarte Rückseite">
  <span class="brand-name">Nordwert</span>
  <p class="name">Jonas Feldmann</p>
  <p class="role">Geschäftsführer</p>
  <p class="address">Lindenweg 12<br>53111 Bonn</p>
  <ul class="contact">
    <li><svg width="5" height="5" viewBox="0 0 10 10"><path d="M2 1l2 2-1 1.5a6 6 0 002.5 2.5L7 6l2 2-1.5 1.5C4.5 9 1 5.5.5 2.5z"/></svg>0228 415520 10</li>
    <li><svg width="5" height="5" viewBox="0 0 10 10"><rect x="1" y="4" width="8" height="4"/><rect x="3" y="1" width="4" height="3"/></svg>0228 415520 19</li>
    <li><svg width="5" height="5" viewBox="0 0 10 10"><rect x="1" y="2" width="8" height="6"/><path d="M1 2l4 3 4-3"/></svg>post@nordwert.eu</li>
    <li><svg width="5" height="5" viewBox="0 0 10 10"><circle cx="5" cy="5" r="4"/><path d="M1 5h8M5 1c-2 2.5-2 5.5 0 8M5 1c2 2.5 2 5.5 0 8"/></svg>www.nordwert.eu</li>
  </ul>
  <div class="band"><span class="g"></span><span class="d"></span></div>
</section>

<section class="piece notebook" aria-label="Notizblock">
  <span class="elastic"></span>
  <span class="brand-name">Nordwert</span>
  <span class="label">Notizblock</span>
  <div class="band"><span class="g"></span><span class="d"></span></div>
</section>
<span class="ribbon"></span>

<section class="piece letterhead" aria-label="Briefpapier">
  <span class="brand-name">Nordwert</span>
  <p class="address">Lindenweg 12<br>53111 Bonn</p>
  <ul class="contact">
    <li><svg width="5" height="5" viewBox="0 0 10 10"><path d="M2 1l2 2-1 1.5a6 6 0 002.5 2.5L7 6l2 2-1.5 1.5C4.5 9 1 5.5.5 2.5z"/></svg>0228 415520 10</li>
    <li><svg width="5" height="5" viewBox="0 0 10 10"><rect x="1" y="4" width="8" height="4"/><rect x="3" y="1" width="4" height="3"/></svg>0228 415520 19</li>
    <li><svg width="5" height="5" viewBox="0 0 10 10"><rect x="1" y="2" width="8" height="6"/><path d="M1 2l4 3 4-3"/></svg>post@nordwert.eu</li>
    <li><svg width="5" height="5" viewBox="0 0 10 10"><circle cx="5" cy="5" r="4"/><path d="M1 5h8M5 1c-2 2.5-2 5.5 0 8M5 1c2 2.5 2 5.5 0 8"/></svg>www.nordwert.eu</li>
  </ul>
  <span class="rule"></span>
  <p class="legal tax">USt.-ID: DE104857362<br>Steuer-Nr.: 205/4172/9061<br>Inhaber: Jonas Feldmann</p>
  <p class="legal bank">Nordbank<br>IBAN: DE71500105170048213<br>BIC: NRDBDEB1XXX</p>
  <div class="band"><span class="g"></span><span class="d"></span></div>
</section>

<section class="piece envelope" aria-label="Briefumschlag C4">
  <span class="brand-name">Nordwert</span>
  <span class="window"></span>
  <div class="band"><span class="g"></span><span class="d"></span></div>
</section>

</body>
</html>
```